Ember Relaywork - Field Service Brochure

We are looking for a one page marketing brochure that includes our rate sheet. I've attached the working we on on the rate page, several photos and several versions of our logo.

```html
<!DOCTYPE html>
<html lang="en">
<head>
<meta charset="utf-8">
<title>Ember Relaywork – Field Service Rates</title>
<link href="https://fonts.googleapis.com/css2?family=Jost:wght@400;500;600;700&display=swap" rel="stylesheet">
<style>
  :root{
    --slate:#5f7a96;
    --slate-light:#7f97b0;
    --orange:#e8692a;
    --orange-light:#f08a3a;
    --panel:#e7e9ed;
    --paper:#ffffff;
    --ink:#7a8797;
    --ink-dark:#4c5a6b;
  }
  *{box-sizing:border-box;margin:0;padding:0}
  html,body{width:1172px;height:1200px;overflow:hidden;background:var(--paper)}
  body{font-family:"Jost",sans-serif;color:var(--ink)}
  .sheet{position:relative;width:1172px;height:1200px;background:var(--paper);overflow:hidden}
  .backdrop{position:absolute;inset:0}
  .hero-photo{position:absolute;top:0;right:0;width:660px;height:330px;
    clip-path:polygon(0 0,100% 0,100% 100%,22% 100%,0 52%);
    background:linear-gradient(160deg,#2f6fc4 0%,#4a8ad6 40%,#8a8f96 62%,#e06a22 85%,#c85a1c 100%)}
  .brand{position:absolute;top:118px;left:60px;display:flex;align-items:center;gap:14px}
  .brand-mark{width:54px;height:54px;background:var(--slate)}
  .brand-name{font-size:30px;font-weight:600;color:var(--slate);letter-spacing:1px;text-transform:uppercase;line-height:1}
  .brand-parent{font-size:12px;font-weight:500;color:var(--slate);margin-top:6px}
  .intro{position:absolute;top:250px;left:60px;width:500px;font-size:20px;line-height:1.45;color:var(--ink)}
  .rate-card{position:absolute;color:#fff;text-align:center;
    clip-path:polygon(14% 0,86% 0,100% 50%,86% 100%,14% 100%,0 50%)}
  .rate-card.premium{top:360px;left:570px;width:540px;height:290px;background:var(--orange)}
  .rate-card.standard{top:540px;left:70px;width:540px;height:290px;background:var(--slate)}
  .rate-head{padding:22px 0 8px;margin:0 40px}
  .premium .rate-head{background:var(--orange-light)}
  .standard .rate-head{background:var(--slate-light)}
  .rate-title{font-size:28px;font-weight:700;line-height:1.2}
  .rate-sub{font-size:14px;width:260px;margin:2px auto 0;line-height:1.2}
  .rate-row{margin:8px 90px 0;padding-bottom:5px;border-bottom:1px solid rgba(255,255,255,.35)}
  .rate-row:last-child{border-bottom:none}
  .rate-price{font-size:21px;font-weight:700;line-height:1.1}
  .rate-note{font-size:13.5px;line-height:1.2}
  .terms{position:absolute;left:60px;width:1060px}
  .terms.expenses{top:846px}
  .terms.minimum{top:970px}
  .terms h2{font-size:23px;font-weight:700;color:var(--orange);line-height:1.2;margin-bottom:4px}
  .terms ul{list-style:none}
  .terms li{font-size:15px;line-height:1.35;color:var(--ink-dark);padding-left:16px;position:relative}
  .terms li::before{content:"";position:absolute;left:2px;top:8px;width:5px;height:5px;border-radius:50%;background:var(--ink-dark)}
  .contact-band{position:absolute;top:1118px;left:0;width:1172px;height:40px;background:var(--slate);
    clip-path:polygon(4% 0,100% 0,100% 100%,0 100%);color:#fff;font-size:15px;display:flex;align-items:center;justify-content:flex-end;padding-right:40px;gap:10px}
  .contact-label{position:absolute;top:1166px;left:60px;font-size:17px;color:var(--ink)}
</style>
</head>
<body>
<main class="sheet">
  <svg class="backdrop" width="1172" height="1200" viewBox="0 0 1172 1200" aria-hidden="true">
    <polygon points="0,820 510,330 1172,330 1172,838 0,838" fill="var(--panel)"/>
    <polygon points="0,820 560,540 600,838 0,838" fill="#dfe2e7"/>
  </svg>

  <div class="hero-photo" role="img" aria-label="Photo of field technicians in an orange lift bucket servicing high-voltage switchgear against a blue sky"></div>

  <header class="brand">
    <div class="brand-mark"></div>
    <div>
      <div class="brand-name">Ember Relaywork</div>
      <div class="brand-parent">A Northline Grid Holdings Company</div>
    </div>
  </header>

  <p class="intro">Ember Relaywork Company offers an expertly trained Field Service program that can provide technical guidance and assistance for your initial installation, sustaining maintenance, and repair of equipment manufactured by Ember Relaywork. A 4-6 week reservation for assistance is recommended to ensure that we can fully accommodate your desired schedule. Expedited service may be available upon request.</p>

  <section class="rate-card premium">
    <div class="rate-head">
      <h2 class="rate-title">Premium Rates</h2>
      <p class="rate-sub">(on-site) over 8 hours + travel and per diem expenses</p>
    </div>
    <div class="rate-row"><div class="rate-price">$250 x 1.50</div><div class="rate-note">= Over Time (9-12 hours) rate per hour</div></div>
    <div class="rate-row"><div class="rate-price">$250 x 2.00</div><div class="rate-note">= Double Time (Over 12 hours) rate per hour</div></div>
    <div class="rate-row"><div class="rate-price">$250 X 2.50</div><div class="rate-note">= Non-standard overnight hours</div></div>
  </section>

  <section class="rate-card standard">
    <div class="rate-head">
      <h2 class="rate-title">Standard Rates</h2>
      <p class="rate-sub">(on-site) up to 10 hours + travel and per diem expenses</p>
    </div>
    <div class="rate-row"><div class="rate-price">$250 x 1.00</div><div class="rate-note">= Monday through Friday rate per hour ($2500 minimum)</div></div>
    <div class="rate-row"><div class="rate-price">$250 x 1.50</div><div class="rate-note">= Saturday rate per hour</div></div>
    <div class="rate-row"><div class="rate-price">$250 X 2.00</div><div class="rate-note">= Sunday rate per hour</div></div>
  </section>

  <section class="terms expenses">
    <h2>Expenses</h2>
    <ul>
      <li>Airfare - invoiced at actual cost + 25%</li>
      <li>Lodging - invoiced at actual cost + 25%</li>
      <li>Meals and Incidentals – invoiced at cost (not to exceed $100/day)</li>
      <li>Rental Vehicle and related costs – invoiced at cost +25%</li>
    </ul>
  </section>

  <section class="terms minimum">
    <h2>Minimum Charge</h2>
    <ul>
      <li>The minimum charge, excluding travel time and expenses shall be the equivalent of one 10 hour day</li>
      <li>Cancellation charge of 4 standard hours plus any non-cancellable airfare or lodging charges shall apply</li>
      <li>Employee Drug Screening</li>
      <li>Drug screening and/or background check costs (if required by customer) shall be invoiced at actual cost plus 30%.</li>
    </ul>
  </section>

  <footer>
    <div class="contact-band">
      <span>1480 Cedar Ridge Rd. S.E.</span><span>•</span><span>Fairhaven, AL 35190</span><span>•</span><span>205-555-0142</span><span>•</span><span>800-555-0177</span><span>•</span><span>Fax: 205-555-0149</span>
    </div>
    <div class="contact-label">Contact us:</div>
  </footer>
</main>
</body>
</html>
```